New business card with our logo

we finalized our logo with the help of pixel harbor - now we need a business card using that logo. we are a metal service center providing raw steel and metal products for fabricating, contractors, artists, etc. we have the wording for the back of the card figured out (attached, no deviations from text please), just need help putting it all together.
would like the look of steel somehow incorporated in the design ... would like the black part of the logo to be steel or silver color (the S & BRANLEY)
Other font styles liked:
- calibri, arial, similar to those, modern looking
Colors
Designer to choose colors to be used in the design.
Requirements
Must have
- Back of card must haves are attached (no deviations from wording please).
- FRONT of card:
- logo
- address
- name
- office tel
- cell
- fax
- website
- address
Nice to have
- incorporate the look of steel or element of steel somehow
- names of the staff on front not in all caps, i.e. Rosvita not ROSVITA
- this industry is more industrial, not coffee or flower shop so design should be aligned with that
- design should be classic and tasteful

```html
<!DOCTYPE html>
<html lang="en">
<head>
<meta charset="utf-8">
<title>Branley Steel – Business Card</title>
<link href="https://fonts.googleapis.com/css2?family=Roboto:wght@400;700&display=swap" rel="stylesheet">
<style>
  :root{
    --page:#2b2620;
    --card-dark:#111214;
    --card-mid:#26282c;
    --steel:#c9ccd1;
    --text:#e6e8eb;
    --blue:#1f7fd0;
    --edge:#1b6fbf;
  }
  *{margin:0;padding:0;box-sizing:border-box}
  html,body{width:1200px;height:840px;overflow:hidden}
  body{background:var(--page);font-family:"Roboto",Arial,sans-serif;position:relative}
  .card{
    position:absolute;width:540px;height:308px;border-radius:18px;overflow:hidden;
    background:
      repeating-linear-gradient(90deg,rgba(255,255,255,.025) 0 1px,transparent 1px 3px),
      linear-gradient(160deg,var(--card-mid) 0%,var(--card-dark) 55%,#1c1d20 100%);
    box-shadow:0 16px 34px rgba(0,0,0,.55);
  }
  .card-back{left:40px;top:120px}
  .card-front{left:620px;top:410px;border-bottom:6px solid var(--edge)}
  .brand{display:flex;align-items:center;gap:12px;position:absolute;left:50%;transform:translateX(-50%);white-space:nowrap}
  .brand-dot{border-radius:50%;border:3px solid var(--steel)}
  .brand-name{font-weight:700;color:var(--steel);letter-spacing:1px}
  .card-back .brand{top:112px}
  .card-back .brand-dot{width:70px;height:70px;border-width:5px}
  .card-back .brand-name{font-size:34px}
  .card-front .brand{top:52px}
  .card-front .brand-dot{width:44px;height:44px}
  .card-front .brand-name{font-size:26px}
  .divider{position:absolute;left:30px;right:30px;top:128px;height:1px;background:var(--blue)}
  .person{position:absolute;left:30px;top:168px;color:var(--text)}
  .person-name{color:var(--blue);font-weight:700;font-size:17px;letter-spacing:.5px}
  .person-role{font-size:12px;margin-top:2px;letter-spacing:.4px}
  .contact{list-style:none;margin-top:10px;font-size:12px}
  .contact li{display:flex;align-items:center;gap:8px;line-height:18px}
  .contact svg{width:11px;height:11px;fill:var(--blue)}
  .location{position:absolute;right:30px;top:144px;text-align:right;color:var(--text);font-size:12px;line-height:17px}
</style>
</head>
<body>
  <section class="card card-back">
    <div class="brand">
      <span class="brand-dot"></span>
      <span class="brand-name">BRANLEY STEEL</span>
    </div>
  </section>

  <section class="card card-front">
    <div class="brand">
      <span class="brand-dot"></span>
      <span class="brand-name">BRANLEY STEEL</span>
    </div>
    <div class="divider"></div>
    <div class="location">
      <p>4120 Foundry Road</p>
      <p>Fairbanks, Alaska 99701</p>
      <p>www.branleysteel.com</p>
    </div>
    <div class="person">
      <p class="person-name">DORIAN KALE</p>
      <p class="person-role">CEO/FOUNDER</p>
      <ul class="contact">
        <li><svg viewBox="0 0 10 10"><path d="M2 0h2l1 2.5-1.3 1a5 5 0 0 0 2.8 2.8l1-1.3L10 6v2a2 2 0 0 1-2 2A8 8 0 0 1 0 2a2 2 0 0 1 2-2z"/></svg>907 214 3086</li>
        <li><svg viewBox="0 0 10 10"><path d="M2.5 0h5a1 1 0 0 1 1 1v8a1 1 0 0 1-1 1h-5a1 1 0 0 1-1-1V1a1 1 0 0 1 1-1zm.5 1.5v6h4v-6z"/></svg>907 538 1172</li>
        <li><svg viewBox="0 0 10 10"><path d="M2 0h5v3H2zM0 3.5h10V8H8v2H2V8H0zm3 3.5v2h4V7z"/></svg>907 214 3090</li>
        <li><svg viewBox="0 0 10 10"><path d="M0 2h10v6H0zm1 1v.4l4 2.6 4-2.6V3z"/></svg>dorian@branleysteel.com</li>
      </ul>
    </div>
  </section>
</body>
</html>
```